Payday Lending App Interface Design

Hello, we are building a payday lending application, Lendoro, that lend people money. I have drafted some of the screens that show the functionalities we have at the moment, please find the screens in attachments.
The elements in the screens are placed just to show what should be included in those screens, it's not necessary to follow the same layout. If you have better design ideas, you are very welcomed to show off your talent.
I think what we want is a style guide so that we can apply the same style to any screens that are similar to the ones I attached. We really like
the style as in the attached image called Style.png. We might want something similar - a simple, clean design yet fun and engaging. Customised graphical elements such as icons, illustrations are preferable.
Apart from the attached screens, we might also need a design for the On Board screen and the Login/Sign Up screen too.
Our logo colour is in yellow and black. Perhaps we will have a similar colour theme. I also attached the logo file, icon-Lendoro.png, if you would like to put it in your design.
Please message me if you need further information.
Regards
Target Market(s)
Young people that doesn't have strong income
Look and feel
Each slider illustrates characteristics of the customer's brand and the style your logo design should communicate.

```html
<!DOCTYPE html>
<html lang="en">
<head>
<meta charset="utf-8">
<title>Lendoro – Payday Lending App Screens</title>
<link href="https://fonts.googleapis.com/css2?family=Poppins:wght@400;500;600;700&display=swap" rel="stylesheet">
<style>
:root{
  --yellow:#fad80f;
  --black:#000;
  --ink:#111;
  --white:#fff;
  --panel:#1c1c1c;
  --panel-row:#363636;
  --field:#f3f3f3;
  --line:#ececec;
  --faint:#c9c9c9;
  --canvas:#ececec;
  --green:#2bbf3a;
  --pink:#f6e6ec;
}
*{box-sizing:border-box;margin:0;padding:0}
html,body{width:1084px;height:1200px;overflow:hidden;background:var(--canvas)}
body{font-family:'Poppins',sans-serif;color:var(--ink)}
.stage{position:relative;width:1821px;height:2016px;transform:scale(.5953);transform-origin:0 0;background:var(--canvas);overflow:hidden}
.phone{position:absolute;width:221px;height:488px;border-radius:30px;background:var(--white);overflow:hidden;box-shadow:0 0 0 1px #e4e4e4}
.phone.short{height:478px}
.bar{height:48px;background:var(--yellow);display:flex;align-items:center;padding:0 10px;gap:8px;font-weight:600;font-size:14px;color:var(--ink)}
.bar .spacer{flex:1}
.body{background:var(--white);border-radius:12px 12px 0 0;margin-top:-8px;position:relative;padding:14px 10px 0}
.dots{display:flex;flex-direction:column;gap:2px}
.dots i{width:3px;height:3px;border-radius:50%;background:var(--ink)}
.nav{position:absolute;left:0;right:0;bottom:0;height:42px;background:var(--white);display:flex;justify-content:space-around;align-items:center;border-top:1px solid #f4f4f4;border-radius:14px 14px 0 0}
.nav .hub{width:26px;height:26px;border-radius:50%;background:var(--yellow);display:flex;align-items:center;justify-content:center}
.btn{display:flex;align-items:center;justify-content:center;gap:6px;background:var(--black);color:var(--yellow);font-weight:600;font-size:13px;border-radius:6px;height:33px}
.field{background:var(--field);border-radius:4px;height:31px;font-size:9px;color:#6a6a6a;display:flex;align-items:center;padding:0 7px;margin-bottom:8px}
.input{border:1px solid #e9e9e9;border-radius:6px;height:34px;font-size:8.5px;color:#444;display:flex;align-items:center;justify-content:space-between;padding:0 10px;margin-bottom:10px;box-shadow:0 2px 4px rgba(0,0,0,.04)}
.brand-mark{display:flex;align-items:center;justify-content:center;gap:6px;font-weight:700;font-size:22px;color:var(--ink)}
.brand-mark .sq{width:16px;height:16px;border-radius:4px;background:var(--yellow)}
.auth{padding:36px 22px 0;text-align:center}
.auth h2{font-size:14.5px;font-weight:600;margin:38px 0 14px}
.auth .or{font-size:7.5px;color:#555;margin:36px 0 14px}
.socials{display:flex;justify-content:center;gap:9px}
.social{width:47px;height:47px;border-radius:8px;background:var(--white);box-shadow:0 2px 8px rgba(0,0,0,.1);display:flex;align-items:center;justify-content:center;font-size:6.5px;font-weight:600;color:var(--ink)}
.auth .foot{font-size:7.5px;margin-top:34px}
.auth .foot b{color:var(--yellow);font-weight:600;text-decoration:underline}
.card{border:1px solid var(--line);border-radius:8px;box-shadow:0 2px 6px rgba(0,0,0,.04)}
.chev{width:6px;height:6px;border-right:1.5px solid currentColor;border-top:1.5px solid currentColor;transform:rotate(45deg);display:inline-block}
.ybtn{width:19px;height:19px;border-radius:4px;background:var(--yellow);display:flex;align-items:center;justify-content:center}
.dark-menu{color:var(--white)}
.dark-menu .row{display:flex;justify-content:space-between;align-items:center;padding:0 16px 0 11px;color:var(--white)}
.settings-list .item{display:flex;align-items:center;gap:12px;height:27px;color:var(--white)}
</style>
</head>
<body>
<div class="stage">

  <!-- Onboarding -->
  <section class="phone short" style="left:330px;top:209px;background:var(--yellow)">
    <svg width="221" height="478" style="position:absolute;inset:0" aria-hidden="true"><circle cx="250" cy="360" r="160" fill="#f5d00a"/></svg>
    <div style="position:relative;text-align:center;padding:80px 16px 0">
      <div style="font-weight:700;font-size:34px;height:72px;display:flex;align-items:center;justify-content:center">Lendoro</div>
      <h1 style="font-size:19.5px;font-weight:600;line-height:1.35;margin-top:24px">Welcome to<br>Payday Lending</h1>
      <p style="font-size:9.3px;line-height:1.25;margin-top:12px">Lorem ipsum dolor sit amet, consectetur adipiscing elit, sed do eiusmod tempor incididunt ut labore et dolore magna aliquais ipsum suspendisse ultrices gravida.</p>
      <div style="display:flex;justify-content:center;gap:6px;margin-top:86px">
        <i style="width:4px;height:4px;border-radius:50%;background:var(--ink)"></i><i style="width:4px;height:4px;border-radius:50%;background:var(--ink)"></i><i style="width:4px;height:4px;border-radius:50%;background:var(--ink)"></i><i style="width:4px;height:4px;border-radius:50%;background:var(--ink)"></i><i style="width:4px;height:4px;border-radius:50%;background:var(--ink)"></i>
      </div>
      <div class="btn" style="margin:24px 8px 0">Get Started Here</div>
    </div>
  </section>

  <!-- Login -->
  <section class="phone short" style="left:639px;top:209px">
    <div class="auth">
      <div class="brand-mark" style="height:68px"><span class="sq"></span>Lendoro</div>
      <h2>Login to your Account</h2>
      <div class="input">Email</div>
      <div class="input">Password <svg width="9" height="6" viewBox="0 0 9 6"><ellipse cx="4.5" cy="3" rx="4" ry="2.6" fill="none" stroke="#444"/><circle cx="4.5" cy="3" r="1.2" fill="#444"/></svg></div>
      <div class="btn" style="margin-top:2px">Sign In</div>
      <p class="or">-Or Sign in With....</p>
      <div class="socials"><span class="social">Searchly</span><span class="social">Friendbook</span><span class="social">Chirpr</span></div>
      <p class="foot">Don't have an Account? <b>Sign Up</b></p>
    </div>
  </section>

  <!-- Sign up -->
  <section class="phone short" style="left:963px;top:209px">
    <div class="auth">
      <div class="brand-mark" style="height:68px"><span class="sq"></span>Lendoro</div>
      <h2>Create your account</h2>
      <div class="input">Email</div>
      <div class="input">Password</div>
      <div class="input">Confirm Password</div>
      <div class="btn" style="margin-top:2px">Sign Up</div>
      <p class="or" style="margin-top:34px">-Or Sign in With....</p>
      <div class="socials"><span class="social">Searchly</span><span class="social">Friendbook</span><span class="social">Chirpr</span></div>
    </div>
  </section>

  <!-- Profile -->
  <section class="phone" style="left:1270px;top:443px;height:489px;background:var(--panel)">
    <div class="bar" style="height:50px"><svg width="13" height="10" viewBox="0 0 13 10"><path d="M12 5H2M5 1L1 5l4 4" fill="none" stroke="#111" stroke-width="1.6"/></svg>Profile<span class="spacer"></span><span class="dots"><i></i><i></i><i></i></span></div>
    <div class="dark-menu" style="background:var(--panel);margin-top:-8px;border-radius:12px 12px 0 0;position:relative;height:447px">
      <div style="display:flex;align-items:center;justify-content:space-between;padding:26px 14px 26px 11px;border-bottom:1px solid #333">
        <div><div style="font-size:13px;color:var(--white)">Hi, Milo Brandt</div><div style="font-size:8px;color:#999">hello@milobrandt.io</div></div>
        <div style="width:51px;height:51px;border-radius:50%;background:#2e2e2e;display:flex;align-items:center;justify-content:center"><svg width="22" height="24" viewBox="0 0 22 24"><circle cx="11" cy="7" r="6" fill="#fad80f"/><path d="M0 24c0-7 5-10 11-10s11 3 11 10z" fill="#fad80f"/></svg></div>
      </div>
      <div style="font-size:10.5px">
        <div class="row" style="height:40px;border-bottom:1px solid #333">Loan Products<span class="chev"></span></div>
        <div class="row" style="height:37px;border-bottom:1px solid #333">Loan History<span class="chev"></span></div>
        <div class="row" style="height:38px">Q&amp;A<span class="chev"></span></div>
        <div class="row" style="height:46px;background:var(--panel-row);border-bottom:1px solid #2a2a2a">Contact Us<span class="chev"></span></div>
        <div class="row" style="height:48px;background:var(--panel-row)">Terms &amp; Conditions<span class="chev"></span></div>
      </div>
      <div style="position:absolute;left:11px;right:11px;bottom:10px;height:60px;border-radius:10px;background:#2d2d2d;display:flex;align-items:center;gap:8px;padding:0 12px;font-size:11px;color:var(--white)"><span style="width:27px;height:27px;border-radius:6px;background:var(--yellow)"></span>Lendoro v.1.0</div>
    </div>
  </section>

  <!-- Personal details -->
  <section class="phone" style="left:330px;top:769px">
    <div class="bar"><svg width="13" height="10" viewBox="0 0 13 10"><path d="M12 5H2M5 1L1 5l4 4" fill="none" stroke="#111" stroke-width="1.6"/></svg>Personal Details<span class="spacer"></span><svg width="10" height="10" viewBox="0 0 10 10"><circle cx="5" cy="5" r="3.4" fill="none" stroke="#111" stroke-width="2.4" stroke-dasharray="2 1"/></svg></div>
    <div class="body" style="padding:20px 10px 0">
      <div class="card" style="padding:14px 9px 18px">
        <div style="font-size:10px;font-weight:600">Personal Details</div>
        <div style="font-size:7.5px;color:var(--faint);line-height:1.1;margin:6px 0 12px;width:150px">Please provide details as shown on ID proof</div>
        <div class="field">Given Name</div><div class="field">Middle Name</div><div class="field">Surname</div><div class="field">Date of Birthday</div><div class="field">Phone Number</div><div class="field">Email Address</div>
        <div class="btn" style="margin-top:26px"><svg width="13" height="13" viewBox="0 0 13 13"><circle cx="6.5" cy="6.5" r="6.5" fill="#fad80f"/><path d="M5 3.5l3 3-3 3" fill="none" stroke="#000" stroke-width="1.6"/></svg>Next</div>
      </div>
    </div>
    <nav class="nav"><svg width="11" height="10"><path d="M1 5L5.5 1 10 5v5H1z" fill="#ddd"/></svg><svg width="11" height="10"><path d="M1 9L4 5l3 2 3-5" fill="none" stroke="#ccc" stroke-width="1.3"/></svg><span class="hub"><svg width="12" height="10" viewBox="0 0 12 10"><path d="M1 3h9M7 0l3 3M11 7H2M5 10L2 7" fill="none" stroke="#111" stroke-width="1.3"/></svg></span><svg width="10" height="10"><circle cx="5" cy="5" r="4" fill="#ddd"/></svg><svg width="11" height="9"><rect width="11" height="9" rx="2" fill="#ddd"/></svg></nav>
  </section>

  <!-- Welcome / progress -->
  <section class="phone" style="left:639px;top:769px">
    <div class="bar" style="height:45px"><svg width="13" height="10" viewBox="0 0 13 10"><path d="M0 1h13M0 5h13M0 9h13" stroke="#111" stroke-width="1.5"/></svg>Welcome!<span class="spacer"></span><svg width="10" height="10" viewBox="0 0 10 10"><circle cx="5" cy="5" r="3.4" fill="none" stroke="#111" stroke-width="2.4" stroke-dasharray="2 1"/></svg></div>
    <div class="body" style="padding:10px 10px 0">
      <div style="display:flex;justify-content:space-between;align-items:center">
        <div><div style="font-size:7.5px;color:#555">Hi, Welcome back</div><div style="font-size:12.5px;font-weight:600">Milo Brandt</div></div>
        <div role="img" aria-label="Portrait photo of the account holder" style="width:49px;height:49px;border-radius:50%;background:linear-gradient(160deg,#c8d3dc,#4d6f8c)"></div>
      </div>
      <div style="position:relative;margin-top:16px;padding-left:18px">
        <svg width="12" height="340" style="position:absolute;left:0;top:0" aria-hidden="true"><line x1="5" y1="14" x2="5" y2="330" stroke="#eee" stroke-width="2"/><circle cx="5" cy="16" r="5.5" fill="#fad80f"/><circle cx="5" cy="57" r="5.5" fill="#fad80f"/><circle cx="5" cy="178" r="5.5" fill="#2bbf3a"/><circle cx="5" cy="216" r="5.5" fill="#fad80f"/><circle cx="5" cy="287" r="5.5" fill="#e6e6e6"/><circle cx="5" cy="322" r="5.5" fill="#e6e6e6"/></svg>
        <div class="card" style="height:31px;display:flex;justify-content:space-between;align-items:center;padding:0 10px 0 12px;font-size:11px">Start<span class="chev"></span></div>
        <div style="background:var(--yellow);border-radius:8px;margin-top:6px;padding:12px 12px 10px;font-size:11px">
          <div style="display:flex;justify-content:space-between;line-height:1.05">Upload Your Personal<br>Information<span class="chev" style="margin-top:3px"></span></div>
          <p style="font-size:7px;line-height:1.3;margin-top:7px">Its seems like your ID documents are expired. Upload your document again to get qualified</p>
          <div class="btn" style="height:21px;font-size:7.5px;margin-top:8px;border-radius:4px">Upload your Documents</div>
        </div>
        <div class="card" style="height:31px;display:flex;justify-content:space-between;align-items:center;padding:0 10px 0 12px;font-size:11px;margin-top:5px">Connect bank account<span class="chev"></span></div>
        <div class="card" style="margin-top:5px;padding:10px 8px 8px 12px">
          <div style="font-size:11px">Apply a loan</div>
          <div style="display:flex;justify-content:space-between;align-items:center;margin-top:4px"><span style="font-size:7px;color:var(--faint);line-height:1.2">Get your loan that<br>fit your need</span><span style="font-size:6.5px;background:#fff6c4;color:#d8c24a;padding:4px 6px;border-radius:3px">Apply Loan</span></div>
        </div>
        <div class="card" style="height:29px;display:flex;justify-content:space-between;align-items:center;padding:0 10px 0 12px;font-size:11px;color:#ddd;margin-top:7px">Repayments<span class="chev"></span></div>
        <div class="card" style="height:29px;display:flex;justify-content:space-between;align-items:center;padding:0 10px 0 12px;font-size:11px;color:#ddd;margin-top:6px">Loan Closed<span class="chev"></span></div>
      </div>
    </div>
    <div style="position:absolute;left:0;right:0;bottom:0;height:16px;border-top:1px solid #eee;border-radius:14px 14px 0 0;background:var(--white)"><span style="position:absolute;left:100px;top:-6px;width:20px;height:20px;border-radius:50%;background:var(--yellow)"></span></div>
  </section>

  <!-- Loan details -->
  <section class="phone" style="left:962px;top:769px">
    <div class="bar"><svg width="13" height="10" viewBox="0 0 13 10"><path d="M12 5H2M5 1L1 5l4 4" fill="none" stroke="#111" stroke-width="1.6"/></svg>Loan Details<span class="spacer"></span><svg width="10" height="10" viewBox="0 0 10 10"><circle cx="5" cy="5" r="3.4" fill="none" stroke="#111" stroke-width="2.4" stroke-dasharray="2 1"/></svg></div>
    <div class="body" style="padding:20px 10px 0">
      <div style="font-size:13px;font-weight:600">Next Repayment</div>
      <div style="background:var(--yellow);border-radius:8px;margin-top:8px;overflow:hidden">
        <div style="padding:14px 14px 10px;display:flex;justify-content:space-between;align-items:center;border-bottom:1px solid #e8c400">
          <div><div style="font-size:22px;font-weight:700">$45,878</div><div style="font-size:8.5px;font-weight:500">Bill Due on 02 Mar</div></div>
          <span class="ybtn" style="background:var(--black)"><span class="chev" style="color:var(--yellow);width:5px;height:5px;margin-left:-2px"></span></span>
        </div>
        <div style="display:flex;padding:8px 14px 12px;gap:50px"><div><div style="font-size:6.5px">Paid Amout</div><div style="font-size:12px;font-weight:600">784733</div></div><div><div style="font-size:6.5px">Unbill Amout</div><div style="font-size:12px;font-weight:600">4733</div></div></div>
      </div>
      <div style="font-size:13px;font-weight:600;margin-top:16px">Activities</div>
      <div class="card" style="height:57px;margin-top:10px;display:flex;justify-content:space-between;align-items:center;padding:0 11px 0 14px"><div><div style="font-size:11px">Repayment</div><div style="font-size:8px;color:#666">01 Mar 2022</div></div><b style="font-size:13px;font-weight:600">$4500</b></div>
      <div class="card" style="height:57px;margin-top:8px;display:flex;justify-content:space-between;align-items:center;padding:0 11px 0 14px"><div><div style="font-size:11px">Repayment</div><div style="font-size:8px;color:#666">01 Mar 2022</div></div><b style="font-size:13px;font-weight:600">$4500</b></div>
      <div class="card" style="height:57px;margin-top:8px;display:flex;justify-content:space-between;align-items:center;padding:0 11px 0 14px"><div><div style="font-size:11px">Repayment</div><div style="font-size:8px;color:#666">01 Mar 2022</div></div><b style="font-size:13px;font-weight:600">$4500</b></div>
    </div>
    <nav class="nav"><svg width="11" height="10"><path d="M1 5L5.5 1 10 5v5H1z" fill="#ddd"/></svg><svg width="11" height="10"><path d="M1 9L4 5l3 2 3-5" fill="none" stroke="#ccc" stroke-width="1.3"/></svg><span class="hub"><svg width="12" height="10" viewBox="0 0 12 10"><path d="M1 3h9M7 0l3 3M11 7H2M5 10L2 7" fill="none" stroke="#111" stroke-width="1.3"/></svg></span><svg width="10" height="10"><circle cx="5" cy="5" r="4" fill="#ddd"/></svg><svg width="11" height="9"><rect width="11" height="9" rx="2" fill="#ddd"/></svg></nav>
  </section>

  <!-- Settings -->
  <section class="phone" style="left:1265px;top:1018px;height:488px;background:var(--black)">
    <div class="bar" style="height:46px"><svg width="13" height="10" viewBox="0 0 13 10"><path d="M12 5H2M5 1L1 5l4 4" fill="none" stroke="#111" stroke-width="1.6"/></svg>Settings<span class="spacer"></span><span class="dots"><i></i><i></i><i></i></span></div>
    <div class="settings-list" style="background:var(--black);margin-top:-8px;border-radius:12px 12px 0 0;font-size:10.5px;position:relative;padding:44px 12px 0">
      <div class="item"><svg width="10" height="11"><circle cx="5" cy="3" r="3" fill="#fad80f"/><path d="M0 11c0-4 2-5 5-5s5 1 5 5z" fill="#fad80f"/></svg>Personal info</div>
      <div class="item"><svg width="10" height="11"><path d="M5 0C2 0 2 3 2 6L0 8h10L8 6c0-3 0-6-3-6zM4 9h2v2H4z" fill="#fad80f"/></svg>Notifications &amp; Emails</div>
      <div class="item"><svg width="10" height="11"><path d="M5 0l5 2c0 5-2 8-5 9C2 10 0 7 0 2z" fill="#fad80f"/></svg>Privacy &amp; Security</div>
      <div style="border-top:1px solid #222;margin:14px -12px 18px"></div>
      <div class="item" style="gap:10px"><svg width="12" height="9"><rect width="12" height="9" rx="1.5" fill="#fad80f"/><rect y="2.5" width="12" height="1.5" fill="#000"/></svg>Bank Accounts</div>
      <div class="item"><svg width="10" height="10"><circle cx="5" cy="5" r="3.4" fill="none" stroke="#fad80f" stroke-width="2.6" stroke-dasharray="2 1"/></svg>Account Settings</div>
      <div class="item" style="gap:14px;height:24px"><svg width="9" height="11"><path d="M2 5V3a2.5 2.5 0 015 0v2" fill="none" stroke="#fad80f" stroke-width="1.5"/><rect y="5" width="9" height="6" rx="1" fill="#fad80f"/></svg>Lock App</div>
      <div class="item" style="height:28px"><svg width="10" height="10"><circle cx="5" cy="5" r="5" fill="#fad80f"/><rect x="4.3" y="4" width="1.4" height="4" fill="#000"/><circle cx="5" cy="2.6" r=".8" fill="#000"/></svg>About</div>
      <div class="item" style="height:26px"><svg width="10" height="10"><path d="M3 2.2A4 4 0 107 2.2" fill="none" stroke="#fad80f" stroke-width="1.4"/><path d="M5 0v5" stroke="#fad80f" stroke-width="1.4"/></svg>Sign out</div>
    </div>
  </section>

  <!-- Bank details -->
  <section class="phone" style="left:330px;top:1354px">
    <div class="bar"><svg width="13" height="10" viewBox="0 0 13 10"><path d="M12 5H2M5 1L1 5l4 4" fill="none" stroke="#111" stroke-width="1.6"/></svg>Bank Details<span class="spacer"></span><span class="dots"><i></i><i></i><i></i></span></div>
    <div class="body" style="padding:20px 10px 0">
      <div class="card" style="height:62px;display:flex;align-items:center;gap:8px;padding:0 10px"><span style="width:36px;height:36px;border-radius:6px;background:var(--pink)"></span><div style="flex:1"><div style="font-size:10px;font-weight:600">Northgate Bank</div><div style="font-size:9px;letter-spacing:.3px">8299348929911</div></div><span class="ybtn"><span class="chev" style="width:5px;height:5px;margin-left:-2px"></span></span></div>
      <div class="card" style="height:62px;display:flex;align-items:center;gap:8px;padding:0 10px;margin-top:14px"><span style="width:36px;height:36px;border-radius:6px;background:#e7f0fb"></span><div style="flex:1"><div style="font-size:10px;font-weight:600">Keelway Bank</div><div style="font-size:9px;letter-spacing:.3px">8299348929911</div></div><span class="ybtn"><span class="chev" style="width:5px;height:5px;margin-left:-2px"></span></span></div>
      <div class="card" style="height:62px;display:flex;align-items:center;gap:8px;padding:0 10px;margin-top:14px"><span style="width:36px;height:36px;border-radius:6px;background:#fdf4d2"></span><div style="flex:1"><div style="font-size:10px;font-weight:600">Harbourline</div><div style="font-size:9px;letter-spacing:.3px">8299348929911</div></div><span class="ybtn"><span class="chev" style="width:5px;height:5px;margin-left:-2px"></span></span></div>
      <div class="btn" style="margin-top:110px"><svg width="13" height="13" viewBox="0 0 13 13"><circle cx="6.5" cy="6.5" r="6.5" fill="#fad80f"/><path d="M6.5 3.5v6M3.5 6.5h6" stroke="#000" stroke-width="1.6"/></svg>Connect Bank Account</div>
    </div>
    <nav class="nav"><svg width="11" height="10"><path d="M1 5L5.5 1 10 5v5H1z" fill="#ddd"/></svg><svg width="11" height="10"><path d="M1 9L4 5l3 2 3-5" fill="none" stroke="#ccc" stroke-width="1.3"/></svg><span class="hub"><svg width="12" height="10" viewBox="0 0 12 10"><path d="M1 3h9M7 0l3 3M11 7H2M5 10L2 7" fill="none" stroke="#111" stroke-width="1.3"/></svg></span><svg width="10" height="10"><circle cx="5" cy="5" r="4" fill="#ddd"/></svg><svg width="11" height="9"><rect width="11" height="9" rx="2" fill="#ddd"/></svg></nav>
  </section>

  <!-- Connecting -->
  <section class="phone" style="left:639px;top:1354px">
    <div style="text-align:center;padding:64px 14px 0">
      <div style="width:97px;height:97px;border-radius:18px;background:var(--pink);margin:0 auto;display:flex;align-items:center;justify-content:center;font-size:11px;font-weight:600">Northgate</div>
      <h2 style="font-size:20px;font-weight:600;line-height:1.3;margin-top:40px">Connecting to<br>your bank</h2>
      <p style="font-size:9.3px;line-height:1.25;margin-top:10px">Please don't exit the app.<br>it takes 3-5 minutes to confirm<br>your details with your bank.</p>
    </div>
    <nav class="nav"><svg width="11" height="10"><path d="M1 5L5.5 1 10 5v5H1z" fill="#ddd"/></svg><svg width="11" height="10"><path d="M1 9L4 5l3 2 3-5" fill="none" stroke="#ccc" stroke-width="1.3"/></svg><span class="hub"><svg width="12" height="10" viewBox="0 0 12 10"><path d="M1 3h9M7 0l3 3M11 7H2M5 10L2 7" fill="none" stroke="#111" stroke-width="1.3"/></svg></span><svg width="10" height="10"><circle cx="5" cy="5" r="4" fill="#ddd"/></svg><svg width="11" height="9"><rect width="11" height="9" rx="2" fill="#ddd"/></svg></nav>
  </section>

  <!-- Connect your bank -->
  <section class="phone" style="left:962px;top:1354px">
    <div class="bar" style="height:50px"><svg width="13" height="10" viewBox="0 0 13 10"><path d="M12 5H2M5 1L1 5l4 4" fill="none" stroke="#111" stroke-width="1.6"/></svg>Connect your Bank<span class="spacer"></span><span class="dots"><i></i><i></i><i></i></span></div>
    <div class="body" style="padding:20px 10px 0">
      <div class="card" style="padding:14px 10px 20px">
        <div style="display:flex;align-items:center;gap:8px;margin-bottom:16px"><span style="width:34px;height:34px;border-radius:6px;background:var(--pink)"></span><div style="flex:1"><div style="font-size:7px;color:var(--faint)">Selected Bank</div><div style="font-size:10px;font-weight:600">Northgate Bank</div></div><svg width="9" height="9"><path d="M1 8l1-3 5-5 2 2-5 5z" fill="#ccc"/></svg></div>
        <div class="field">Account Number</div><div class="field">Confirm Account Number</div><div class="field">Holder Name</div><div class="field">Password</div><div class="field">Phone Number<span style="color:var(--faint)">(Optional)</span></div>
        <div class="btn" style="margin-top:26px"><svg width="13" height="13" viewBox="0 0 13 13"><circle cx="6.5" cy="6.5" r="6.5" fill="#fad80f"/><path d="M3.5 6.5l2 2 4-4" fill="none" stroke="#000" stroke-width="1.6"/></svg>Connect</div>
      </div>
    </div>
    <nav class="nav"><svg width="11" height="10"><path d="M1 5L5.5 1 10 5v5H1z" fill="#ddd"/></svg><svg width="11" height="10"><path d="M1 9L4 5l3 2 3-5" fill="none" stroke="#ccc" stroke-width="1.3"/></svg><span class="hub"><svg width="12" height="10" viewBox="0 0 12 10"><path d="M1 3h9M7 0l3 3M11 7H2M5 10L2 7" fill="none" stroke="#111" stroke-width="1.3"/></svg></span><svg width="10" height="10"><circle cx="5" cy="5" r="4" fill="#ddd"/></svg><svg width="11" height="9"><rect width="11" height="9" rx="2" fill="#ddd"/></svg></nav>
  </section>
</div>
</body>
</html>
```